New Business Cards
Tiller Frame LLC
Project: New Business Cards
New Business Cards - Transportation
Creative Brief
Professional
Glen Hadwick
President
4817 Cedar Knoll Road Green Bay, WI 54311
glen@tillerframe-example.com
www.TillerFrame-example.com www.socialhub-example/TillerFrameLLC
I would like to keep my company address off this card as I haven't setup a PO Box yet. I want to focus on my website and facebook page. Would like to see a rendering of a card without my last name. I don't know what I want so bring everything you have. Thanks for all the work on this.
Like to have a picture of my product and company web/facebook address.

```html
<!DOCTYPE html>
<html lang="en">
<head>
<meta charset="utf-8">
<title>Tiller Frame LLC – Business Cards</title>
<link href="https://fonts.googleapis.com/css2?family=Libre+Baskerville&family=Roboto:wght@400;700&display=swap" rel="stylesheet">
<style>
  :root {
    --backdrop: #e6e6e8;
    --card: #ffffff;
    --red: #d3151c;
    --red-dark: #a80d12;
    --ink: #3a3a3c;
    --grey: #8a8a8d;
    --grey-light: #c9c9cc;
  }
  * { box-sizing: border-box; margin: 0; padding: 0; }
  html, body { width: 1200px; height: 864px; overflow: hidden; }
  body {
    background: var(--backdrop);
    font-family: "Roboto", Arial, sans-serif;
    position: relative;
  }
  .card {
    position: absolute;
    top: 278px;
    width: 540px;
    height: 308px;
    background: var(--card);
    border-radius: 18px;
    box-shadow: 0 6px 18px rgba(0,0,0,0.12);
    overflow: hidden;
  }
  .card-back { left: 40px; }
  .card-front { left: 620px; }

  .brand {
    display: flex;
    align-items: center;
    gap: 10px;
  }
  .brand-dot {
    width: 22px; height: 22px;
    border-radius: 50%;
    background: var(--red);
  }
  .brand-name {
    font-family: "Roboto", Arial, sans-serif;
    font-weight: 700;
    color: var(--ink);
    letter-spacing: 0.06em;
    text-transform: uppercase;
    white-space: nowrap;
  }

  .card-back .brand {
    position: absolute;
    left: 0; right: 0; top: 112px;
    justify-content: center;
  }
  .card-back .brand-name { font-size: 26px; }
  .back-web {
    position: absolute;
    left: 0; right: 0; top: 172px;
    text-align: center;
    font-size: 11px;
    letter-spacing: 0.35em;
    color: var(--grey);
    white-space: nowrap;
  }
  .back-web strong { color: var(--red); font-weight: 700; }

  .front-art { position: absolute; inset: 0; }
  .card-front .brand {
    position: absolute;
    left: 42px; top: 170px;
  }
  .card-front .brand-name { font-size: 30px; }

  .person {
    position: absolute;
    right: 34px; top: 128px;
    text-align: right;
    font-family: "Libre Baskerville", Georgia, serif;
    font-variant: small-caps;
    color: var(--red);
    white-space: nowrap;
  }
  .person-name { font-size: 17px; letter-spacing: 0.04em; }
  .person-title { font-size: 13px; color: var(--grey); letter-spacing: 0.06em; }

  .contacts {
    position: absolute;
    left: 42px; top: 222px;
    list-style: none;
    font-size: 10.5px;
    color: var(--red-dark);
    letter-spacing: 0.05em;
    text-transform: uppercase;
  }
  .contacts li {
    display: flex; align-items: center; gap: 7px;
    height: 17px;
    white-space: nowrap;
  }
  .contact-icon { width: 11px; height: 11px; flex: none; }
</style>
</head>
<body>

<section class="card card-back" aria-label="Card back">
  <div class="brand">
    <span class="brand-dot"></span>
    <span class="brand-name">Tiller Frame</span>
  </div>
  <p class="back-web">www.<strong>TILLERFRAME</strong>-example.com</p>
</section>

<section class="card card-front" aria-label="Card front">
  <svg class="front-art" viewBox="0 0 540 308" width="540" height="308" aria-hidden="true">
    <path d="M110 0 H540 V160 C480 78 330 28 110 0 Z" fill="var(--red)"/>
    <path d="M200 0 H540 V60 C460 24 340 8 200 0 Z" fill="var(--red-dark)" opacity="0.35"/>
    <path d="M40 168 C120 100 250 64 410 54 C270 76 150 112 40 168 Z" fill="var(--grey)"/>
    <path d="M70 160 C150 112 260 86 380 76 C260 94 160 122 70 160 Z" fill="var(--grey-light)"/>
  </svg>

  <div class="brand">
    <span class="brand-dot"></span>
    <span class="brand-name">Tiller Frame</span>
  </div>

  <div class="person">
    <p class="person-name">Glen Hadwick</p>
    <p class="person-title">President</p>
  </div>

  <ul class="contacts">
    <li>
      <svg class="contact-icon" viewBox="0 0 12 12"><circle cx="6" cy="6" r="6" fill="var(--red)"/><path d="M4 3 L5 3 L5.6 4.6 L4.9 5.2 C5.3 6 6 6.7 6.8 7.1 L7.4 6.4 L9 7 L9 8 C9 8.5 8.5 9 8 9 C5.2 8.8 3.2 6.8 3 4 C3 3.5 3.5 3 4 3 Z" fill="#fff"/></svg>
      555-014-2290
    </li>
    <li>
      <svg class="contact-icon" viewBox="0 0 12 12"><circle cx="6" cy="6" r="6" fill="var(--red)"/><rect x="3" y="4" width="6" height="4.2" fill="none" stroke="#fff" stroke-width="0.9"/><path d="M3 4 L6 6.4 L9 4" fill="none" stroke="#fff" stroke-width="0.9"/></svg>
      glen@tillerframe-example.com
    </li>
    <li>
      <svg class="contact-icon" viewBox="0 0 12 12"><circle cx="6" cy="6" r="6" fill="var(--red)"/><circle cx="6" cy="6" r="3" fill="none" stroke="#fff" stroke-width="0.9"/><path d="M3 6 H9 M6 3 C4.6 4.6 4.6 7.4 6 9 M6 3 C7.4 4.6 7.4 7.4 6 9" fill="none" stroke="#fff" stroke-width="0.7"/></svg>
      www.TillerFrame-example.com
    </li>
    <li>
      <svg class="contact-icon" viewBox="0 0 12 12"><circle cx="6" cy="6" r="6" fill="var(--red)"/></svg>
      www.socialhub-example/TillerFrameLLC
    </li>
  </ul>
</section>

</body>
</html>
```